Silver Reed Signage

Please I'm looking to have signage for business front door and 2 windows. Wow me! It is the first thing ppl will see always.
I'm looking to have some privacy because I am in the beauty business, so privacy is key. Please look at attached pictures of front and windows. Make it elegant because the spa shop is all about luxury excellence. I need website, Email address phone number in name of the company. I'd like to also put some services somewhere on the signage (s) you can place it where you'd think it would be best. Lymphatic Drainage, Body Sculpting/contouring, Detoxing, Cavitation, Facials ..... and much more

```html
<!DOCTYPE html>
<html lang="en">
<head>
<meta charset="utf-8">
<title>Silver Reed Signage</title>
<link rel="stylesheet" href="https://fonts.googleapis.com/css2?family=Josefin+Sans:wght@400;600&family=Ubuntu:wght@400&family=Montserrat:wght@500&display=swap">
<style>
  :root {
    --stage: #6b6b6b;
    --violet: #5b1ff0;
    --violet-soft: #7448f4;
    --deep: #2d14a8;
    --white: #ffffff;
    --frame: #111111;
  }
  html, body { margin: 0; padding: 0; overflow: hidden; }
  body { width: 1200px; height: 1001px; background: var(--stage); position: relative; }
  .panel { position: absolute; background: var(--violet); color: var(--white); overflow: hidden; }
  .ornament { position: absolute; display: block; }
  .center { position: absolute; left: 0; right: 0; text-align: center; margin: 0; }
  .brand { font-family: "Josefin Sans", sans-serif; font-weight: 600; letter-spacing: -0.5px; line-height: 1; }
  .mark { position: absolute; border-radius: 50%; background: var(--deep); }
  .divider { position: absolute; height: 1px; background: var(--deep); }

  /* Suite sign */
  .suite-sign { left: 116px; top: 159px; width: 221px; height: 62px; }
  .suite-sign .label { font-family: "Josefin Sans", sans-serif; font-size: 30px; top: 16px; letter-spacing: 1px; }

  /* Door */
  .door-panel { left: 138px; top: 294px; width: 178px; height: 532px; }
  .door-panel .mark { left: 46px; top: 120px; width: 86px; height: 86px; }
  .door-panel .brand { font-size: 32px; top: 230px; }
  .door-panel .tagline { font-family: "Montserrat", sans-serif; font-weight: 500; font-size: 11.5px; line-height: 15.5px; top: 308px; letter-spacing: 0.3px; }
  .door-panel .divider { left: 38px; width: 102px; top: 366px; background: var(--white); }
  .door-panel .contact { font-family: "Ubuntu", sans-serif; font-size: 10px; line-height: 15.5px; top: 380px; }
  .door-panel .contact .phone { font-size: 11.5px; }

  /* Services window */
  .services-panel { left: 370px; top: 158px; width: 268px; height: 600px; }
  .services-panel .service { font-family: "Ubuntu", sans-serif; font-size: 19.5px; line-height: 20px; letter-spacing: 0.2px; }

  /* Upper window */
  .brand-panel { left: 657px; top: 146px; width: 445px; height: 200px; }
  .brand-panel .mark { left: 181px; top: 30px; width: 78px; height: 78px; }
  .brand-panel .brand { font-size: 25px; top: 118px; }
  .brand-panel .tagline { font-family: "Montserrat", sans-serif; font-weight: 500; font-size: 6.5px; top: 142px; letter-spacing: 0.3px; }
  .brand-panel .web { font-family: "Ubuntu", sans-serif; font-size: 14px; top: 168px; letter-spacing: 0.3px; }
</style>
</head>
<body>

  <section class="panel suite-sign">
    <p class="center label">SUITE F</p>
  </section>

  <section class="panel door-panel">
    <svg class="ornament" style="left:74px;top:0" width="104" height="82" role="img" aria-label="Line-drawn leafy branch with berries">
      <defs><linearGradient id="leafA" x1="1" y1="0" x2="0" y2="1"><stop offset="0" stop-color="#7448f4"/><stop offset="1" stop-color="#5b1ff0"/></linearGradient></defs>
      <rect width="104" height="82" fill="url(#leafA)"/>
    </svg>
    <div class="mark"></div>
    <p class="center brand">SILVER<br>REED</p>
    <p class="center tagline">WHERE BEAUTY<br>WELLNESS FIND<br>HARMONY</p>
    <div class="divider"></div>
    <p class="center contact"><span class="phone">(212) 555-0187</span><br>contact@silverreed.com<br>www.silverreed.com</p>
    <svg class="ornament" style="left:0;top:450px" width="118" height="82" role="img" aria-label="Line-drawn flower and leaves">
      <defs><linearGradient id="leafB" x1="0" y1="1" x2="1" y2="0"><stop offset="0" stop-color="#7448f4"/><stop offset="1" stop-color="#5b1ff0"/></linearGradient></defs>
      <rect width="118" height="82" fill="url(#leafB)"/>
    </svg>
  </section>

  <section class="panel services-panel">
    <svg class="ornament" style="left:0;top:0" width="114" height="86" role="img" aria-label="Line-drawn leafy branch with bud">
      <defs><linearGradient id="leafC" x1="0" y1="0" x2="1" y2="1"><stop offset="0" stop-color="#7448f4"/><stop offset="1" stop-color="#5b1ff0"/></linearGradient></defs>
      <rect width="114" height="86" fill="url(#leafC)"/>
    </svg>
    <p class="center service" style="top:176px">Lymphatic Drainage</p>
    <div class="divider" style="left:85px;width:98px;top:207px"></div>
    <p class="center service" style="top:220px">Body Sculpting<br>Contouring</p>
    <div class="divider" style="left:85px;width:98px;top:271px"></div>
    <p class="center service" style="top:285px">Detoxing</p>
    <div class="divider" style="left:85px;width:98px;top:314px"></div>
    <p class="center service" style="top:321px">Cavitation</p>
    <div class="divider" style="left:85px;width:98px;top:350px"></div>
    <p class="center service" style="top:358px">Facials</p>
    <div class="divider" style="left:85px;width:98px;top:387px"></div>
    <p class="center service" style="top:394px">...and Much More</p>
    <svg class="ornament" style="left:46px;top:446px" width="222" height="154" role="img" aria-label="Line-drawn leaves and berry sprigs">
      <defs><linearGradient id="leafD" x1="0" y1="0" x2="0" y2="1"><stop offset="0" stop-color="#5b1ff0"/><stop offset="1" stop-color="#7448f4"/></linearGradient></defs>
      <rect width="222" height="154" fill="url(#leafD)"/>
    </svg>
  </section>

  <section class="panel brand-panel">
    <svg class="ornament" style="left:0;top:0" width="73" height="52" role="img" aria-label="Line-drawn flower and leaves">
      <defs><linearGradient id="leafE" x1="0" y1="0" x2="1" y2="1"><stop offset="0" stop-color="#7448f4"/><stop offset="1" stop-color="#5b1ff0"/></linearGradient></defs>
      <rect width="73" height="52" fill="url(#leafE)"/>
    </svg>
    <div class="mark"></div>
    <p class="center brand">SILVER REED</p>
    <p class="center tagline">WHERE BEAUTY WELLNESS FIND HARMONY</p>
    <p class="center web">www.silverreed.com</p>
    <svg class="ornament" style="left:343px;top:122px" width="102" height="78" role="img" aria-label="Line-drawn leafy branch with bud">
      <defs><linearGradient id="leafF" x1="1" y1="1" x2="0" y2="0"><stop offset="0" stop-color="#7448f4"/><stop offset="1" stop-color="#5b1ff0"/></linearGradient></defs>
      <rect width="102" height="78" fill="url(#leafF)"/>
    </svg>
  </section>

</body>
</html>
```